Self Watering Planter Packaging

We would like to create a unique Retail Packaging for our Self Watering Planter.
It is a Cedar Planter that is a Self Watering Cedar Planter that has a fountain.
It has a long lasting battery that last 3 months watering every other day.
Programable Automatic Watering System
Fountain Oxygenates the water Keeping the fresh water flowing and prevents stagnate smelly water.
No more root Rot because the System Aerates the Roots every time you water. Just like it does in nature.
Patented System that waters from the bottom up
No Power Cords
No Solar Panels
No Plumbing
I have put the old packaging that we had for our first version. We want something much better than this. We want this to be slanted to urban living, and being able to grow anywhere,
This system is guaranteed to grow amazing plants, fruits and vegetables.
Packaging size will be 36"L x 4"x12"
We will want a matching sell sheet to go along with this as well.
Reason: I have extended the Deadline
Anyone that likes to garden but may not have the land to garden. Herb Gardens, Urban Gardens, etc.
Retail

```html
<!DOCTYPE html>
<html lang="en">
<head>
<meta charset="utf-8">
<title>Cedar Row's Grow Station – Box Dieline</title>
<link href="https://fonts.googleapis.com/css2?family=Oswald:wght@400;600&family=Dancing+Script:wght@600&display=swap" rel="stylesheet">
<style>
  :root{
    --green:#0b7a55;
    --green-dark:#08654a;
    --white:#ffffff;
    --brick:#eceae8;
    --brick-shade:#d9d7d5;
    --floor:#c9c9c9;
    --line:#c8c8c8;
    --ink:#2b2b2b;
  }
  *{margin:0;padding:0;box-sizing:border-box}
  html,body{width:874px;height:1200px;overflow:hidden;background:var(--white)}
  .canvas{position:relative;width:874px;height:1200px;background:var(--white)}
  .dieline{position:absolute;left:0;top:326px;width:1093px;height:700px;transform:scale(.8);transform-origin:0 0}
  .dieline > *{position:absolute}
  .flap{background:var(--white);border:1px solid var(--line)}
  .flap-green{background:var(--green)}
  .panel{overflow:hidden}
  .panel > *{position:absolute}
  .panel-front{background:linear-gradient(180deg,var(--brick) 0%,#f4f3f2 60%,var(--floor) 82%,#b8b8b8 100%)}
  .panel-side{background:var(--green)}
  .glue{background:var(--white);border:1px solid var(--line);border-left:none;clip-path:polygon(0 0,100% 6%,100% 94%,0 100%)}

  .brand{font-family:'Oswald',sans-serif;font-weight:600;text-align:center;line-height:1.05;letter-spacing:.5px}
  .brand .name{display:block;font-size:21px}
  .brand .product{display:block;font-size:17px}
  .brand-dark{color:var(--ink)}
  .brand-light{color:var(--white)}

  .script{font-family:'Dancing Script',cursive;font-weight:600}
  .tagline{color:var(--ink);font-size:12px;line-height:1.25;text-align:center}
  .side-title{color:var(--white);font-size:14px;text-align:center;width:100%;left:0}

  .ribbon{background:var(--green);color:var(--white);font-family:'Oswald',sans-serif;font-weight:600;font-size:7px;line-height:1.05;text-align:center;padding-top:6px;clip-path:polygon(0 0,100% 0,100% 100%,50% 82%,0 100%)}

  .photo{border-radius:3px}
  .icon{background:var(--green);border-radius:3px;display:flex;align-items:center;justify-content:center}
  .caption{font-family:'Oswald',sans-serif;font-weight:400;font-size:4.6px;line-height:1.2;color:var(--ink);text-align:center;border-bottom:.6px solid var(--ink);padding-bottom:2px}
  .badge{border-radius:50%;background:var(--green);border:2px solid var(--white);color:var(--white);font-family:'Oswald',sans-serif;font-size:6px;text-align:center;display:flex;flex-direction:column;justify-content:center;line-height:1.3}
  .tile-label{font-family:'Oswald',sans-serif;font-size:6.5px;color:var(--white);text-align:center;background:rgba(0,0,0,.35);width:100%;bottom:0;left:0;padding:2px 0}
  .diagram-note{font-family:'Oswald',sans-serif;font-size:4.6px;line-height:1.25;color:var(--white);text-align:center}
  .upside{transform:rotate(180deg)}
</style>
</head>
<body>
<div class="canvas">
  <div class="dieline">

    <!-- top flaps -->
    <div class="flap" style="left:73px;top:103px;width:290px;height:100px"></div>
    <div class="flap" style="left:369px;top:103px;width:162px;height:100px"></div>
    <div class="flap-green panel" style="left:535px;top:35px;width:294px;height:168px">
      <div class="brand brand-light" style="left:0;top:58px;width:100%"><span class="name">Cedar Row's</span><span class="product">GROW STATION</span></div>
    </div>
    <div class="flap" style="left:831px;top:103px;width:162px;height:100px"></div>

    <!-- front panel A -->
    <div class="panel panel-front" style="left:73px;top:203px;width:290px;height:278px">
      <div class="brand brand-dark" style="left:30px;top:18px;width:125px"><span class="name">Cedar Row's</span><span class="product">GROW STATION</span></div>
      <div class="ribbon" style="left:210px;top:0;width:37px;height:37px">GROW YOUR GARDEN ANYWHERE!</div>
      <div class="script tagline" style="left:30px;top:77px;width:110px">Grow Station<br>Self-Watering Garden<br>Planter Fountain</div>
      <div class="photo" role="img" aria-label="Cedar planter on legs filled with lavender and flowering plants" style="left:12px;top:120px;width:155px;height:122px;background:linear-gradient(180deg,#6f8a4e 0%,#8a7fa8 30%,#b98a58 60%,#c79a67 100%)"></div>
      <div class="badge" style="left:62px;top:217px;width:60px;height:60px">Bubbling Fountain<br>Oxygenates Plants</div>

      <div class="photo" role="img" aria-label="Ripe tomatoes on the vine" style="left:181px;top:65px;width:38px;height:38px;background:radial-gradient(circle,#d8402a,#8a2a1a 70%,#3f6b2a)"></div>
      <div class="icon" style="left:237px;top:65px;width:39px;height:38px">
        <svg width="24" height="24" viewBox="0 0 24 24" fill="none" stroke="#fff" stroke-width="2"><circle cx="12" cy="13" r="8"/><path d="M12 13V8M12 13l3 2M10 3h4"/></svg>
      </div>
      <div class="caption" style="left:172px;top:108px;width:56px">Perfect For Herbs, Vegetables, Flowers, Endless Possibilities!</div>
      <div class="caption" style="left:229px;top:108px;width:56px">Programmable Run Times For Various Watering Needs</div>

      <div class="icon" style="left:181px;top:135px;width:38px;height:38px">
        <svg width="24" height="24" viewBox="0 0 24 24" fill="none" stroke="#fff" stroke-width="2" stroke-linecap="round"><path d="M3 9h11a3 3 0 1 0-3-3M3 14h15a3 3 0 1 1-3 3M3 19h6"/></svg>
      </div>
      <div class="icon" style="left:237px;top:135px;width:39px;height:38px">
        <svg width="22" height="24" viewBox="0 0 22 24"><path d="M11 2C8 8 4 11 4 16a7 7 0 0 0 14 0c0-5-4-8-7-14z" fill="#cfe9f6"/><path d="M8 17a3 3 0 0 0 3 3" stroke="#fff" stroke-width="1.5" fill="none"/></svg>
      </div>
      <div class="caption" style="left:172px;top:178px;width:56px">Aerates Roots Between Watering</div>
      <div class="caption" style="left:229px;top:178px;width:56px">Waters From The Bottom Up</div>

      <div class="icon" style="left:217px;top:202px;width:37px;height:38px">
        <svg width="20" height="24" viewBox="0 0 20 24"><rect x="3" y="4" width="14" height="18" rx="2" fill="#9d9d95"/><rect x="7" y="1" width="6" height="3" fill="#9d9d95"/></svg>
      </div>
      <div class="caption" style="left:205px;top:245px;width:60px">Powered By A Powerful Rechargeable Battery</div>
    </div>

    <!-- side panel B -->
    <div class="panel panel-side" style="left:367px;top:203px;width:164px;height:278px">
      <div class="brand brand-light" style="left:0;top:15px;width:100%"><span class="name">Cedar Row's</span><span class="product">GROW STATION</span></div>
      <div class="script side-title" style="top:72px">Endless Growing Possibilities!</div>
      <div class="photo" role="img" aria-label="Planter with lavender" style="left:17px;top:95px;width:63px;height:80px;background:linear-gradient(180deg,#8a86b8,#7a6a4a 60%,#a07a4e)"><span class="tile-label">Lavender</span></div>
      <div class="photo" role="img" aria-label="Planter with flowers" style="left:85px;top:95px;width:63px;height:80px;background:linear-gradient(180deg,#c0574a,#7a8a4a 45%,#a07a4e)"><span class="tile-label">Flowers</span></div>
      <div class="photo" role="img" aria-label="Planter with succulents" style="left:17px;top:180px;width:63px;height:80px;background:linear-gradient(180deg,#7e9a6e,#4a4a3a 60%,#3a342c)"><span class="tile-label">Succulents</span></div>
      <div class="photo" role="img" aria-label="Planter with vegetables" style="left:85px;top:180px;width:63px;height:80px;background:linear-gradient(180deg,#5e8a3e,#4a4a3a 60%,#3a342c)"><span class="tile-label">Vegetables</span></div>
    </div>

    <!-- front panel C -->
    <div class="panel panel-front" style="left:535px;top:203px;width:294px;height:278px">
      <div class="brand brand-dark" style="left:30px;top:18px;width:125px"><span class="name">Cedar Row's</span><span class="product">GROW STATION</span></div>
      <div class="ribbon" style="left:212px;top:0;width:37px;height:37px">GROW YOUR GARDEN ANYWHERE!</div>
      <div class="script tagline" style="left:30px;top:77px;width:110px">Grow Station<br>Self-Watering Garden<br>Planter Fountain</div>
      <div class="photo" role="img" aria-label="Cedar planter on legs filled with lavender and flowering plants" style="left:12px;top:120px;width:155px;height:122px;background:linear-gradient(180deg,#6f8a4e 0%,#8a7fa8 30%,#b98a58 60%,#c79a67 100%)"></div>
      <div class="badge" style="left:62px;top:217px;width:60px;height:60px">Bubbling Fountain<br>Oxygenates Plants</div>

      <div class="photo" role="img" aria-label="Ripe tomatoes on the vine" style="left:181px;top:65px;width:38px;height:38px;background:radial-gradient(circle,#d8402a,#8a2a1a 70%,#3f6b2a)"></div>
      <div class="icon" style="left:237px;top:65px;width:39px;height:38px">
        <svg width="24" height="24" viewBox="0 0 24 24" fill="none" stroke="#fff" stroke-width="2"><circle cx="12" cy="13" r="8"/><path d="M12 13V8M12 13l3 2M10 3h4"/></svg>
      </div>
      <div class="caption" style="left:172px;top:108px;width:56px">Perfect For Herbs, Vegetables, Flowers, Endless Possibilities!</div>
      <div class="caption" style="left:229px;top:108px;width:56px">Programmable Run Times For Various Watering Needs</div>

      <div class="icon" style="left:181px;top:135px;width:38px;height:38px">
        <svg width="24" height="24" viewBox="0 0 24 24" fill="none" stroke="#fff" stroke-width="2" stroke-linecap="round"><path d="M3 9h11a3 3 0 1 0-3-3M3 14h15a3 3 0 1 1-3 3M3 19h6"/></svg>
      </div>
      <div class="icon" style="left:237px;top:135px;width:39px;height:38px">
        <svg width="22" height="24" viewBox="0 0 22 24"><path d="M11 2C8 8 4 11 4 16a7 7 0 0 0 14 0c0-5-4-8-7-14z" fill="#cfe9f6"/><path d="M8 17a3 3 0 0 0 3 3" stroke="#fff" stroke-width="1.5" fill="none"/></svg>
      </div>
      <div class="caption" style="left:172px;top:178px;width:56px">Aerates Roots Between Watering</div>
      <div class="caption" style="left:229px;top:178px;width:56px">Waters From The Bottom Up</div>

      <div class="icon" style="left:217px;top:202px;width:37px;height:38px">
        <svg width="20" height="24" viewBox="0 0 20 24"><rect x="3" y="4" width="14" height="18" rx="2" fill="#9d9d95"/><rect x="7" y="1" width="6" height="3" fill="#9d9d95"/></svg>
      </div>
      <div class="caption" style="left:205px;top:245px;width:60px">Powered By A Powerful Rechargeable Battery</div>
    </div>

    <!-- side panel D -->
    <div class="panel panel-side" style="left:831px;top:203px;width:162px;height:278px">
      <div class="brand brand-light" style="left:0;top:15px;width:100%"><span class="name">Cedar Row's</span><span class="product">GROW STATION</span></div>
      <div class="script side-title" style="top:76px;font-size:12px">Patented Self - Watering System</div>
      <div class="photo" role="img" aria-label="Cross-section diagram of planter watering roots from below" style="left:37px;top:102px;width:89px;height:57px;background:linear-gradient(180deg,#3f8a3a 0%,#5aa044 35%,#6a4a32 55%,#5a3c28 80%,#3a7fc0 100%)"></div>
      <div class="diagram-note" style="left:30px;top:163px;width:103px">When the Fountain turns on, it automatically waters plants from the bottom up</div>
      <div class="photo" role="img" aria-label="Cross-section diagram of planter with lowered water letting air reach roots" style="left:37px;top:187px;width:89px;height:57px;background:linear-gradient(180deg,#3f8a3a 0%,#5aa044 35%,#6a4a32 55%,#5a3c28 85%,#8fc3e8 100%)"></div>
      <div class="diagram-note" style="left:30px;top:248px;width:103px">When the Fountain turns off, the water level drops and allows air to oxygenate the roots between</div>
    </div>

    <!-- glue flap -->
    <div class="glue" style="left:993px;top:205px;width:24px;height:276px"></div>

    <!-- bottom flaps -->
    <div class="flap" style="left:73px;top:481px;width:290px;height:100px"></div>
    <div class="flap" style="left:369px;top:481px;width:162px;height:100px"></div>
    <div class="flap-green panel" style="left:535px;top:481px;width:294px;height:167px">
      <div class="brand brand-light upside" style="left:0;top:58px;width:100%"><span class="name">Cedar Row's</span><span class="product">GROW STATION</span></div>
    </div>
    <div class="flap" style="left:831px;top:481px;width:162px;height:100px"></div>

  </div>
</div>
</body>
</html>
```